I need a business card representing my company, VELDRA, it's an artist management and design company. Complete name is "VELDRA Artist Mgmt. + Design Co." I need it to be world class and very appealing, sophisticated and artistically unique.
Updates

Posted an updated Brief please see. I need a business card representing my company, VELDRA, it's an artist management and design company. Complete name is "VELDRA Artist Mgmt. + Design Co." I need it to be world class and very appealing, sophisticated and artistically unique.

Designs look the same

Designs look the same

Target Market(s)

Advertisers, Entertainment Companies, Commercial companies

Industry/Entity Type

Advertising

Contact Information for Business Card

I need a business card representing my company, VELDRA, it's an artist management and design company. Complete name is "VELDRA Artist Mgmt. + Design Co." I need it to be world class and very appealing, sophisticated and artistically unique. One side can be VELDRA Artist Mgmt. + Design Co. and the other my name, Teodoro Lindqvist, my contact telephone: 412.638.2957, email veldraartist@plumora.net, my address: 3264 Harwell Ave. #517 Miami, FL 33184

Font styles to use
Other font styles liked:
• Calibri

Colors
ffffff
0455a3
f37122

Requirements
Must have
• "VELDRA" stand out bigger than the rest of the text.
Nice to have
• Name "VELDRA" can be centered on one side or in the corner or along side edges, just need something cool and different.
Should not have
• I am open just try to keep it clean looking

```html
<!DOCTYPE html>
<html lang="en">
<head>
<meta charset="utf-8">
<title>VELDRA Business Card</title>
<link rel="stylesheet" href="https://fonts.googleapis.com/css2?family=Roboto+Condensed:wght@700&family=Arimo:wght@400;700&family=Didact+Gothic&family=Great+Vibes&display=swap">
<style>
  :root {
    --blue: #1656a0;
    --orange: #f37122;
    --ink: #000000;
    --paper: #ffffff;
    --skyline-tone: #e6e6e6;
  }
  html, body {
    margin: 0;
    padding: 0;
    width: 1200px;
    height: 1000px;
    overflow: hidden;
    background: var(--paper);
  }
  .canvas {
    position: relative;
    width: 1200px;
    height: 1000px;
  }
  .card {
    position: absolute;
    left: 26px;
    width: 876px;
    height: 464px;
    border: 3px solid var(--ink);
    background: var(--paper);
    overflow: hidden;
  }
  .card--front { top: 22px; }
  .card--back { top: 507px; }

  .skyline-area {
    position: absolute;
    left: 0;
    right: 0;
    top: 250px;
    bottom: 0;
    background: linear-gradient(180deg, #eeeeee 0%, var(--skyline-tone) 100%);
  }
  .wordmark {
    position: absolute;
    left: 0;
    top: 0;
  }
  .wordmark text {
    font-family: "Roboto Condensed", "Arial Narrow", sans-serif;
    font-weight: 700;
    fill: var(--blue);
  }
  .tagline {
    position: absolute;
    right: 28px;
    top: 190px;
    margin: 0;
    font-size: 26px;
    white-space: nowrap;
    color: var(--ink);
  }
  .tagline__company {
    font-family: "Arimo", Arial, sans-serif;
    font-weight: 700;
    color: var(--orange);
  }
  .tagline__divider,
  .tagline__web {
    font-family: "Didact Gothic", "Century Gothic", sans-serif;
  }

  .mission {
    position: absolute;
    left: 29px;
    top: 24px;
    margin: 0;
    font-family: "Didact Gothic", "Century Gothic", sans-serif;
    font-size: 34px;
    line-height: 42px;
    color: var(--ink);
  }
  .mission__lead {
    font-variant: small-caps;
    font-size: 36px;
  }
  .mission__strong {
    font-family: "Arimo", Arial, sans-serif;
    font-weight: 700;
  }
  .mission__region {
    font-family: "Great Vibes", cursive;
    font-size: 54px;
    line-height: 54px;
    vertical-align: -6px;
  }

  .contact {
    position: absolute;
    right: 28px;
    top: 310px;
    text-align: right;
    font-family: "Arimo", Arial, sans-serif;
    color: var(--ink);
  }
  .contact__name {
    margin: 0 0 4px;
    font-size: 42px;
    line-height: 48px;
    font-weight: 400;
  }
  .contact__first {
    font-family: "Didact Gothic", "Century Gothic", sans-serif;
    color: var(--orange);
  }
  .contact__last {
    font-weight: 700;
    color: var(--blue);
  }
  .contact__line {
    margin: 0;
    font-size: 25px;
    line-height: 38px;
    white-space: nowrap;
  }
  .contact__bold { font-weight: 700; }
</style>
</head>
<body>
<main class="canvas">
  <section class="card card--front">
    <div class="skyline-area" role="img" aria-label="Outline illustration of the Miami city skyline"></div>
    <svg class="wordmark" width="876" height="190" viewBox="0 0 876 190" aria-label="VELDRA">
      <text x="158" y="182" font-size="232" textLength="686" lengthAdjust="spacingAndGlyphs">VELDRA</text>
    </svg>
    <p class="tagline">
      <span class="tagline__company">Artist Mgmt. + Design Co</span>
      <span class="tagline__divider">|</span>
      <span class="tagline__web">www.veldradesignco.net</span>
    </p>
  </section>

  <section class="card card--back">
    <p class="mission">
      <span class="mission__lead">Original products</span><br>
      designed by <span class="mission__strong">local artists</span><br>
      insipred by the local chic<br>
      lifestyles and the melting pot<br>
      of <span class="mission__region">South Florida.</span>
    </p>
    <div class="contact">
      <h1 class="contact__name"><span class="contact__first">Teodoro</span> <span class="contact__last">Lindqvist</span></h1>
      <p class="contact__line">412.638.2957 | <span class="contact__bold">veldraartist@plumora.net</span></p>
      <p class="contact__line">3264 Harwell Ave. #517 | <span class="contact__bold">Miami, FL 33184</span></p>
    </div>
  </section>
</main>
</body>
</html>
```